Business Card Design

Looking for a professional looking business card for a carpentry/construction business that deals with renovations, extensions, homes, and anything carpentry based in Northern Australia. Would like to incorporate the attached logo with backgrounds of white, grey or maybe a close up of timber/wood grain. Thanks

Industry/Entity Type

Carpentry

Contact Information for Business Card

Dean Carlow, Owner, Po Box 2674 Katherine NT 0851, dean-carlow@fernmail.example, 0419563072, Builders Number: 293417CR

Requirements
Should not have
• Power tools/hand tools related to carpentry

```html
<!DOCTYPE html>
<html lang="en">
<head>
<meta charset="utf-8">
<title>Carlow Carpentry – Business Card</title>
<link rel="stylesheet" href="https://fonts.googleapis.com/css2?family=Questrial&family=Arimo:wght@400&display=swap">
<style>
  :root {
    --card-bg: #ffffff;
    --ink-blue: #2358a8;
    --brand-blue: #1f5fb4;
    --brand-accent: #29abe2;
  }
  * { margin: 0; padding: 0; box-sizing: border-box; }
  html, body {
    width: 1200px;
    height: 741px;
    overflow: hidden;
    background: var(--card-bg);
  }
  .card {
    position: relative;
    width: 1200px;
    height: 741px;
    background: var(--card-bg);
    color: var(--ink-blue);
  }
  .brand {
    position: absolute;
    left: 712px;
    top: 128px;
    display: flex;
    align-items: center;
    gap: 16px;
  }
  .brand-mark {
    width: 22px;
    height: 22px;
    background: var(--brand-accent);
  }
  .brand-name {
    font-family: "Arimo", Arial, sans-serif;
    font-weight: 400;
    font-size: 44px;
    line-height: 1;
    color: var(--brand-blue);
    white-space: nowrap;
  }
  .identity {
    position: absolute;
    left: 62px;
    top: 216px;
    font-family: "Questrial", "Century Gothic", sans-serif;
  }
  .identity .name {
    font-size: 51px;
    line-height: 1;
    font-weight: 400;
  }
  .identity .role {
    font-size: 33px;
    line-height: 1;
    font-style: italic;
    margin-top: 8px;
  }
  .contact {
    position: absolute;
    left: 62px;
    top: 404px;
    font-family: "Arimo", Arial, sans-serif;
    font-size: 29px;
    line-height: 44px;
  }
  .business {
    position: absolute;
    left: 68px;
    top: 584px;
    font-family: "Arimo", Arial, sans-serif;
    font-size: 29px;
    line-height: 45px;
  }
</style>
</head>
<body>
  <main class="card">
    <div class="brand">
      <span class="brand-mark" aria-hidden="true"></span>
      <span class="brand-name">Carlow Carpentry</span>
    </div>

    <section class="identity">
      <h1 class="name">Dean Carlow</h1>
      <p class="role">Owner</p>
    </section>

    <section class="contact">
      <p class="phone">0419563072</p>
      <p class="email">dean-carlow@fernmail.example</p>
    </section>

    <section class="business">
      <p class="address">Po Box 2674, Katherine NT 0851.</p>
      <p class="licence">Builders Number: 293417CR</p>
    </section>
  </main>
</body>
</html>
```